Design a Brochure for Bellmora Group

Bellmora Group, consists of 3 divisions, Bellmora Property Investments, Bellmora Private Wealth and Bellmora Home Loans. Each with their own colour combination (see the attached brochures)

we need to get a more suitable corporate brochure designed, taking a look at the actual look of the brochure as well as the content. I have uploaded a short version and long version of the brochure. They will need to run side by side. The A3 folded, will be generally handed out whilst the longer version is only for serious clients, as the cost of producing is too great to just randomly distribute.

experience in the property investment and financial industry, would be a huge advantage.

```html
<!DOCTYPE html>
<html lang="en">
<head>
<meta charset="utf-8">
<title>Bellmora Group Brochure</title>
<link href="https://fonts.googleapis.com/css2?family=Arimo:wght@400;700&display=swap" rel="stylesheet">
<style>
:root{
  --blue:#1c3f94;
  --blue-deep:#132c72;
  --blue-night:#0f2461;
  --yellow:#f6b90f;
  --white:#ffffff;
  --paper:#f3f5f9;
  --ink-soft:#c9d4ef;
  --stage:#e8e9ec;
}
*{box-sizing:border-box;margin:0;padding:0}
html,body{width:1200px;height:544px;overflow:hidden}
body{background:var(--stage);font-family:"Arimo",Arial,sans-serif;position:relative}
.brochure{position:absolute;left:40px;top:90px;width:1120px;height:365px;display:flex;box-shadow:0 6px 18px rgba(0,0,0,.18)}
.panel{position:relative;height:100%;overflow:hidden;background:var(--blue);color:var(--white)}
.panel--one{width:184px}
.panel--two{width:184px;background:var(--blue-deep)}
.panel--three{width:185px}
.panel--back{width:251px;background:var(--blue-night)}
.panel--cover{width:316px;background:var(--paper)}
.photo{position:absolute}
.tri{position:absolute}
.copy{position:absolute;font-size:4.6px;line-height:1.45;color:var(--ink-soft)}
.copy p{margin-bottom:4px}
.copy ul{list-style:none;margin:2px 0 4px 4px}
.copy h3{font-size:6.5px;color:var(--white);font-weight:700;margin:4px 0 3px}
.brand{position:absolute;font-weight:400;white-space:nowrap}
.contact{position:absolute;left:20px;right:20px;text-align:center}
.contact__lead{font-size:5px;color:var(--ink-soft)}
.contact__phone{font-size:10px;font-weight:700;color:var(--yellow);line-height:1.3}
.contact__fax{font-size:7.5px;font-weight:700;color:var(--white)}
.contact__small{font-size:4.5px;color:var(--ink-soft);line-height:1.6}
.warning{position:absolute;left:30px;right:30px;top:265px;text-align:center;font-size:4.4px;line-height:1.5;color:var(--ink-soft)}
.warning h4{font-size:6.5px;color:var(--white);margin-bottom:3px}
.divisions{position:absolute;left:8px;top:37px;font-size:5.5px;color:var(--blue-deep)}
.tagline{position:absolute;left:0;right:0;bottom:0;height:48px;background:var(--yellow);padding:8px 0 0 24px;color:var(--blue-deep);font-weight:700;font-size:13px;line-height:1.1}
</style>
</head>
<body>
<div class="brochure">

  <section class="panel panel--one">
    <div class="photo" role="img" aria-label="Photo of a smiling family" style="left:0;top:0;width:184px;height:66px;background:linear-gradient(135deg,#7fa6d6,#d7b59a 60%,#5a7fb8)"></div>
    <svg class="tri" style="left:0;top:0" width="184" height="66" viewBox="0 0 184 66"><polygon points="118,66 184,66 184,22" fill="var(--yellow)"/></svg>
    <div class="brand" style="left:10px;top:34px;font-size:12px">Bellmora</div>
    <div class="copy" style="left:10px;right:10px;top:80px">
      <p>Bellmora Group helps clients build lasting wealth through careful research, sound education and honest analysis of every opportunity we present.</p>
      <h3 style="color:var(--yellow)">Research Education Analysis</h3>
    </div>
    <div class="photo" role="img" aria-label="Photo of a couple reviewing plans" style="left:10px;top:128px;width:60px;height:44px;background:linear-gradient(135deg,#c9a78c,#6d8fbf)"></div>
    <svg class="tri" style="left:0;top:124px" width="184" height="52" viewBox="0 0 184 52"><polygon points="74,4 184,4 184,48" fill="var(--yellow)"/></svg>
    <div class="copy" style="left:10px;right:10px;top:184px">
      <p>We take the time to understand your goals before recommending any property or investment strategy.</p>
      <p>Our approach is built on the following principles:</p>
      <ul><li>Independent research</li><li>Clear education</li><li>Ongoing analysis</li><li>Transparent fees</li><li>Long term planning</li></ul>
    </div>
  </section>

  <section class="panel panel--two">
    <div class="copy" style="left:10px;right:10px;top:12px">
      <p>Property has long been one of the most reliable ways to grow wealth across generations. Our team selects homes in areas with strong growth and rental demand.</p>
    </div>
    <div class="photo" role="img" aria-label="Photo of a modern family home" style="left:40px;top:60px;width:144px;height:62px;background:linear-gradient(180deg,#8fb3dc,#c8b08a 70%,#6b8a4a)"></div>
    <svg class="tri" style="left:0;top:56px" width="184" height="70" viewBox="0 0 184 70"><polygon points="0,4 40,4 40,66" fill="var(--yellow)"/><polygon points="150,66 184,66 184,40" fill="var(--yellow)"/></svg>
    <div class="copy" style="left:10px;right:10px;top:134px">
      <p>Every purchase is backed by a full report on location, price history and future supply.</p>
    </div>
    <div class="photo" role="img" aria-label="Photo of hands signing documents" style="left:40px;top:170px;width:144px;height:56px;background:linear-gradient(135deg,#b8915f,#e0cdb0 50%,#7d6a9c)"></div>
    <svg class="tri" style="left:0;top:166px" width="184" height="64" viewBox="0 0 184 64"><polygon points="0,4 40,4 40,60" fill="var(--yellow)"/></svg>
    <div class="copy" style="left:10px;right:10px;top:240px">
      <h3>Exceptional service</h3>
      <p>From first meeting to settlement, a dedicated adviser guides you through each step and stays in touch long after.</p>
    </div>
  </section>

  <section class="panel panel--three">
    <svg class="tri" style="left:0;top:0" width="185" height="110" viewBox="0 0 185 110"><polygon points="0,0 185,0 185,95 50,95 0,40" fill="var(--white)"/><polygon points="110,30 185,30 185,95 150,95" fill="var(--yellow)"/></svg>
    <div class="photo" role="img" aria-label="Photo of a hand holding a pen" style="left:150px;top:34px;width:35px;height:30px;background:linear-gradient(135deg,#d9c2a3,#8a9ab8)"></div>
    <div class="brand" style="left:48px;top:44px;font-size:14px;color:var(--blue)">Bellmora</div>
    <div class="copy" style="left:10px;right:10px;top:104px">
      <p>Our private wealth team works alongside your accountant to shape a plan that fits your income, your family and your future.</p>
      <h3 style="color:var(--yellow)">We call this unique process</h3>
      <h3>The Bellmora 6 STEPS TO SUCCESS</h3>
      <ul><li>1. Discover your goals</li><li>2. Review your position</li><li>3. Research the market</li><li>4. Build your strategy</li><li>5. Secure the finance</li><li>6. Review every year</li></ul>
      <p style="color:var(--white)">Start your free review today</p>
    </div>
    <div class="photo" role="img" aria-label="Photo of a hiker resting on a rock above a green valley" style="left:0;top:246px;width:185px;height:119px;background:linear-gradient(180deg,#a9c8e6,#d8e6ee 35%,#8aa869 65%,#5d7a3e)"></div>
    <svg class="tri" style="left:0;top:240px" width="185" height="40" viewBox="0 0 185 40"><polygon points="0,0 185,0 0,36" fill="var(--blue)"/></svg>
  </section>

  <section class="panel panel--back">
    <div class="contact" style="top:26px">
      <p class="contact__lead">You can visit us at one of the following address:</p>
      <p class="contact__lead">Head Office: Level 12, Harbour House, 40 Quay Street, Sydney NSW 2000</p>
      <p class="contact__phone" style="margin-top:8px;font-size:8px">You can always call us on:</p>
      <p class="contact__phone">Ph: 1300 555 014</p>
      <p class="contact__fax">Fax: 1300 555 015</p>
      <p class="contact__small" style="margin-top:6px">or email us at<br><b style="color:var(--white)">hello@bellmoragroup.example</b><br>or visit our website<br><b style="color:var(--white)">www.bellmoragroup.example</b></p>
      <p class="contact__small" style="margin-top:8px">Bellmora Private Wealth Pty Ltd is an authorised representative.</p>
    </div>
    <div class="warning">
      <h4>NO ADVICE WARNING</h4>
      <p>The information in this brochure is general in nature and does not consider your personal situation. Seek independent advice before acting on it.</p>
    </div>
  </section>

  <section class="panel panel--cover">
    <div class="brand" style="left:112px;top:12px;font-size:20px;color:var(--blue)">Bellmora</div>
    <svg class="tri" style="left:0;top:0" width="316" height="130" viewBox="0 0 316 130"><polygon points="0,34 316,34 316,46 0,110" fill="var(--yellow)"/><polygon points="0,46 316,46 316,70 0,130" fill="var(--blue)"/></svg>
    <p class="divisions">Home Loans | Property Investments | Private Wealth</p>
    <div class="photo" role="img" aria-label="Photo of a couple facing a staircase rising into a cloudy sky" style="left:0;top:70px;width:316px;height:247px;background:linear-gradient(180deg,#1e4fa0,#6d9fd4 40%,#c9dcef 70%,#8fa6b8)"></div>
    <svg class="tri" style="left:0;top:60px" width="316" height="70" viewBox="0 0 316 70"><polygon points="0,0 316,0 316,10 0,70" fill="var(--blue)"/></svg>
    <div class="tagline">Building a brighter<br>future,today....</div>
  </section>

</div>
</body>
</html>
```